Website Comps for Famous Southern BBQ Restaurant in Alabama

We need an authentic, brand-focused redesign for a restaurant.

We need an authentic look.
The client really likes this website.
https://pelzerpit.com/

I don't want to see a bunch of crazy colors.
Avoid image sliders on the homepage. I hate those.

Please mockup the following three pages:
Homepage
Interior page (for mockup purposes, you can do an About page)
Menu page

I only need the PSD's; not the website coded.

Here is the current website: www.dunmoresmokehouse.com

https://pelzerpit.com/

Here are some additional stock photos. New photos will be shot, but these may help for your mock-up designs.
https://www.filecrate.net/sh/83kqvtrpe21zwa9/QXM71bTr4-plWnfVoe8KtYjd?dl=0
Updates

I realize we don't have a lot of high-quality photos to work with.Those will be shot.Here are some additional stock photos that may help.https://www.filecrate.net/sh/83kqvtrpe21zwa9/QXM71bTr4-plWnfVoe8KtYjd?dl=0 Added Saturday, June 10, 2017

Target Market(s)

United states

Industry/Entity Type

Restaurant

Number of Pages Required

3 page

Font styles to use
Sans Serif

Colors

Designer to choose colors to be used in the design.

Requirements
Must have
• An authentic look.
• The client really likes this website.
• https://pelzerpit.com/
• It's simple, bold, and vintage at the same time.
• That is what we want.
• Our existing website is
• dunmoresmokehouse.com
Nice to have
• Simplicity. Something that makes the food look good.
• Possibly a background.
• Logo:
• https://www.filecrate.net/s/k58tnwpl3ovza2e/dunmore-smokehouse-ridgeway.png?dl=0
• Here is a sampling of photos for your comps:
• https://www.filecrate.net/sh/61vbqzhoewpxtn4/QLT4b8JKyRmPPwf6c2ZnHUVpe?dl=0
Should not have
• Nothing too busy.
• Not too many colors.
• Keep it simple, authentic, "down home."
• No homepage image sliders.

```html
<!DOCTYPE html>
<html lang="en">
<head>
<meta charset="utf-8">
<title>Dunmore Smokehouse — Home</title>
<link rel="stylesheet" href="https://fonts.googleapis.com/css2?family=Oswald:wght@400;500;600&family=Open+Sans:wght@400;600&display=swap">
<style>
:root{
  --orange:#f5a11c;
  --brown:#4a1505;
  --brown-deep:#3a0f03;
  --cream:#fbeed8;
  --cream-light:#fdf6ea;
  --card:#f7e4c7;
  --ink:#3b2a20;
  --text:#5a4a40;
  --white:#ffffff;
}
*{box-sizing:border-box;margin:0;padding:0}
html,body{width:1200px;height:2575px;overflow:hidden}
body{position:relative;background:var(--white);font-family:"Open Sans",sans-serif;color:var(--text)}
.abs{position:absolute}
.heading{font-family:"Oswald",sans-serif;font-weight:500}

/* header */
.site-header{left:0;top:0;width:1200px;height:70px}
.brand{left:150px;top:9px;width:62px;height:60px;background:var(--brown);display:flex;align-items:center;justify-content:center;text-align:center;font-family:"Oswald",sans-serif;font-size:11px;line-height:13px;color:var(--orange);font-weight:500;text-transform:uppercase}
.main-nav{left:326px;top:22px;display:flex;gap:13px;font-family:"Oswald",sans-serif;font-size:15px;color:var(--ink);text-transform:uppercase}
.main-nav .active{color:var(--orange);border-top:2px solid var(--orange);padding-top:2px;margin-top:-4px}
.btn-product{left:916px;top:15px;width:132px;height:37px;background:var(--brown);color:var(--white);font-family:"Oswald",sans-serif;font-size:15px;display:flex;align-items:center;justify-content:center;border-radius:2px}

/* hero */
.hero{left:130px;top:85px;width:942px;height:392px}
.hero-photo{left:145px;top:100px;width:910px;height:360px;background:linear-gradient(180deg,#0f2131 0%,#1d3346 40%,#5a3a2a 62%,#b4643a 78%,#3a2a24 100%)}
.hero-title{left:145px;top:214px;width:910px;text-align:center;font-family:"Oswald",sans-serif;font-weight:500;font-size:26px;color:var(--orange);text-transform:uppercase;letter-spacing:.2px}

/* about */
.about-bg{left:0;top:480px;width:1200px;height:480px;background:linear-gradient(180deg,#fff 0%,#fff 60%,var(--cream-light) 100%)}
.about-title{left:150px;top:503px;font-size:29px;color:var(--brown)}
.person{left:150px;width:510px}
.person-name{display:flex;align-items:center;gap:6px;font-family:"Oswald",sans-serif;font-size:19px;color:var(--orange)}
.person-name svg{flex:none}
.person-bio{margin-left:20px;margin-top:3px;font-size:10px;line-height:12.5px;color:var(--text)}
.btn-story{left:151px;top:864px;width:131px;height:36px;background:var(--brown);color:var(--white);font-family:"Oswald",sans-serif;font-size:14px;display:flex;align-items:center;justify-content:center;border-radius:2px}
.owner-photo{left:667px;top:514px;width:382px;height:384px;border:5px solid var(--orange);background:linear-gradient(160deg,#8a6e56 0%,#a68a6e 40%,#6e5c4e 100%)}

/* locations */
.loc-card{top:995px;width:190px;height:258px;background:var(--card)}
.loc-frame{left:12px;top:12px;width:166px;height:234px;border:1.5px solid var(--brown);border-radius:10px}
.loc-name{position:absolute;left:0;top:28px;width:190px;text-align:center;font-family:"Oswald",sans-serif;font-weight:500;font-size:15px;line-height:18px;color:var(--brown);text-transform:uppercase}
.loc-photo{position:absolute;left:42px;top:70px;width:106px;height:106px;border-radius:50%;border:3px solid var(--orange)}
.loc-btn{position:absolute;left:34px;top:202px;width:122px;height:30px;background:var(--orange);color:var(--white);font-family:"Oswald",sans-serif;font-size:13px;display:flex;align-items:center;justify-content:center}

/* street kitchen */
.street{left:0;top:1304px;width:1200px;height:500px;background:radial-gradient(ellipse at 55% 65%,#4a2a14 0%,#22150d 35%,#0c0907 70%,#050505 100%)}
.street-title{left:0;top:1498px;width:1200px;text-align:center;font-size:24px;color:var(--white)}
.street-rule{left:540px;top:1544px;width:120px;height:2px;background:var(--white)}
.street-text{left:210px;top:1555px;width:780px;text-align:center;font-size:18px;line-height:26px;color:var(--white)}

/* hours */
.hours-card{top:1858px;width:185px;height:193px;background:#fff;border:1px solid #eee3d3;box-shadow:0 1px 3px rgba(0,0,0,.06)}
.hours-title{position:absolute;left:30px;top:20px;display:flex;align-items:center;gap:10px;font-family:"Oswald",sans-serif;font-size:23px;color:var(--orange)}
.hours-line{position:absolute;left:28px;font-size:12px;line-height:16px;color:var(--ink)}
.hours-band{position:absolute;left:0;bottom:0;width:100%;height:52px;background:var(--orange);color:var(--white);font-size:12px;line-height:15px;display:flex;align-items:center;padding-left:14px;gap:6px}

/* news */
.news-bg{left:0;top:2100px;width:1200px;height:430px;background:var(--cream)}
.news-edge{left:0;top:2086px}
.news-title{left:0;top:2130px;width:1200px;text-align:center;font-size:29px;color:var(--brown)}
.news-item{top:2199px;width:294px}
.news-photo{width:294px;height:187px}
.news-item h3{font-family:"Oswald",sans-serif;font-weight:500;font-size:18px;color:var(--brown);margin-top:16px}
.news-item p{font-size:12.5px;line-height:17px;color:var(--text);margin-top:2px;width:285px}

/* footer */
.site-footer{left:0;top:2526px;width:1200px;height:49px;background:var(--brown-deep)}
.copyright{left:150px;top:2544px;font-family:"Oswald",sans-serif;font-size:11px;color:var(--white);text-transform:uppercase}
.footer-nav{right:150px;top:2544px;display:flex;gap:10px;font-family:"Oswald",sans-serif;font-size:10.5px;color:var(--white);text-transform:uppercase}
</style>
</head>
<body>

<header class="abs site-header">
  <div class="abs brand">Dunmore<br>Smoke<br>house</div>
  <nav class="abs main-nav">
    <span class="active">Home</span><span>About</span><span>Locations</span><span>Restaurant Menus</span><span>Catering</span><span>News</span><span>Store</span><span>Contact Us</span>
  </nav>
  <div class="abs btn-product">Our Product</div>
</header>

<section>
  <svg class="abs hero" viewBox="0 0 942 392" aria-hidden="true">
    <path d="M10 8 L930 6 L938 40 L926 90 L934 200 L928 330 L935 372 L880 388 L600 384 L300 390 L40 386 L8 360 L16 250 L6 120 L14 60 Z" fill="#0b0d10"/>
  </svg>
  <div class="abs hero-photo" role="img" aria-label="Ribs and pork shoulders smoking on a grill grate over glowing coals"></div>
  <h1 class="abs hero-title">Pork-stuffed tater named in “100 plates to try down south”</h1>
</section>

<section>
  <div class="abs about-bg"></div>
  <h2 class="abs heading about-title">About Us</h2>

  <div class="abs person" style="top:568px">
    <div class="person-name"><svg width="18" height="8" viewBox="0 0 18 8"><path d="M0 4H14" stroke="#4a1505" stroke-width="2"/><path d="M12 0L18 4L12 8Z" fill="#4a1505"/></svg>Wade Porter</div>
    <p class="person-bio">Porter opened his original Dunmore Smokehouse in Ridgeway’s Linwood neighborhood in 2009, and opened Dunmore Soul Kitchen with chef and co-owner Curtis Hale in Eastlake.</p>
  </div>
  <div class="abs person" style="top:648px">
    <div class="person-name"><svg width="18" height="8" viewBox="0 0 18 8"><path d="M0 4H14" stroke="#4a1505" stroke-width="2"/><path d="M12 0L18 4L12 8Z" fill="#4a1505"/></svg>Curtis Hale</div>
    <p class="person-bio">Former chef de cuisine at Harbor Room, is Dunmore Soul Kitchen executive chef and part-owner.</p>
  </div>
  <div class="abs person" style="top:717px">
    <div class="person-name"><svg width="18" height="8" viewBox="0 0 18 8"><path d="M0 4H14" stroke="#4a1505" stroke-width="2"/><path d="M12 0L18 4L12 8Z" fill="#4a1505"/></svg>Russell Tate</div>
    <p class="person-bio">Co-owner of Dunmore Juke Joint, former owner Marlow’s Oysters &amp; Steaks in the same Hillcrest Commons shopping center.</p>
  </div>
  <div class="abs person" style="top:797px">
    <div class="person-name"><svg width="18" height="8" viewBox="0 0 18 8"><path d="M0 4H14" stroke="#4a1505" stroke-width="2"/><path d="M12 0L18 4L12 8Z" fill="#4a1505"/></svg>Jesse Lowry</div>
    <p class="person-bio">Country Voices winner Lowry was a co-owner of Ember.</p>
  </div>
  <div class="abs btn-story">Dunmore’s Story</div>
  <div class="abs owner-photo" role="img" aria-label="Owner seated at a diner table beneath vintage signs"></div>
</section>

<section>
  <div class="abs loc-card" style="left:245px">
    <div class="abs loc-frame"></div>
    <div class="loc-name">Dunmore Smokehouse-<br>Linwood</div>
    <div class="loc-photo" style="background:linear-gradient(180deg,#c33a2a,#e9d8b8 60%,#8a5a3a)" role="img" aria-label="Storefront of the Linwood restaurant"></div>
    <div class="loc-btn">Read More</div>
  </div>
  <div class="abs loc-card" style="left:506px">
    <div class="abs loc-frame"></div>
    <div class="loc-name">Dunmore Soul Kitchen -<br>Eastlake</div>
    <div class="loc-photo" style="background:linear-gradient(180deg,#6fa3d8,#3f7bbd 60%,#2b3e5c)" role="img" aria-label="Restaurant sign against a blue sky in Eastlake"></div>
    <div class="loc-btn">Read More</div>
  </div>
  <div class="abs loc-card" style="left:765px">
    <div class="abs loc-frame"></div>
    <div class="loc-name">Dunmore Juke Joint -<br>Hillcrest</div>
    <div class="loc-photo" style="background:linear-gradient(180deg,#6a4a36,#b0744a 55%,#3a2a22)" role="img" aria-label="Interior of the Hillcrest juke joint with a flag on the wall"></div>
    <div class="loc-btn">Read More</div>
  </div>
</section>

<section>
  <div class="abs street" role="img" aria-label="Pitmaster tending a glowing wood-fired smoker in a dark kitchen"></div>
  <h2 class="abs heading street-title">Dunmore’s Street Kitchen</h2>
  <div class="abs street-rule"></div>
  <p class="abs street-text">Dunmore Smokehouse on Wheels...Serving Lunch Daily with Catering for Parties, Events &amp; Just About Anything Else!</p>
</section>

<section>
  <div class="abs hours-card" style="left:275px">
    <div class="hours-title"><svg width="24" height="22" viewBox="0 0 24 22"><path d="M1 3L8 0L16 3L23 0V19L16 22L8 19L1 22Z" fill="#4a1505"/><path d="M8 0V19M16 3V22" stroke="#fff" stroke-width="1.5"/></svg>Location</div>
    <div class="hours-line" style="top:68px"><svg width="9" height="11" viewBox="0 0 9 11"><path d="M4.5 0A4.5 4.5 0 0 1 9 4.5C9 7 4.5 11 4.5 11S0 7 0 4.5A4.5 4.5 0 0 1 4.5 0Z" fill="#3b2a20"/><circle cx="4.5" cy="4.5" r="1.6" fill="#fff"/></svg> 2140 Pinecrest Road<br>&nbsp;&nbsp;&nbsp;Ridgeway AL 35990</div>
    <div class="hours-line" style="top:108px"><svg width="10" height="10" viewBox="0 0 10 10"><path d="M2 0L4 2.5L3 4Q4.5 6.5 6 7L7.5 6L10 8L8.5 10Q3 9 0 1.5Z" fill="#3b2a20"/></svg> (205) 555-0143</div>
    <div class="hours-band"><svg width="11" height="11" viewBox="0 0 11 11"><circle cx="5.5" cy="5.5" r="4.6" fill="none" stroke="#fff" stroke-width="1.4"/><path d="M5.5 2.5V5.5H8" stroke="#fff" stroke-width="1.4" fill="none"/></svg> Mon - Sat: 11:00 am - 8 pm</div>
  </div>
  <div class="abs hours-card" style="left:500px">
    <div class="hours-title"><svg width="24" height="22" viewBox="0 0 24 22"><path d="M1 3L8 0L16 3L23 0V19L16 22L8 19L1 22Z" fill="#4a1505"/><path d="M8 0V19M16 3V22" stroke="#fff" stroke-width="1.5"/></svg>Location</div>
    <div class="hours-line" style="top:68px"><svg width="9" height="11" viewBox="0 0 9 11"><path d="M4.5 0A4.5 4.5 0 0 1 9 4.5C9 7 4.5 11 4.5 11S0 7 0 4.5A4.5 4.5 0 0 1 4.5 0Z" fill="#3b2a20"/><circle cx="4.5" cy="4.5" r="1.6" fill="#fff"/></svg> 2140 Pinecrest Road<br>&nbsp;&nbsp;&nbsp;Ridgeway AL 35990</div>
    <div class="hours-line" style="top:108px"><svg width="10" height="10" viewBox="0 0 10 10"><path d="M2 0L4 2.5L3 4Q4.5 6.5 6 7L7.5 6L10 8L8.5 10Q3 9 0 1.5Z" fill="#3b2a20"/></svg> (205) 555-0143</div>
    <div class="hours-band"><svg width="11" height="11" viewBox="0 0 11 11"><circle cx="5.5" cy="5.5" r="4.6" fill="none" stroke="#fff" stroke-width="1.4"/><path d="M5.5 2.5V5.5H8" stroke="#fff" stroke-width="1.4" fill="none"/></svg> <span>Mon - Sat: 11:00 am - 8 pm<br>Sun: 11:00 am - 4 pm</span></div>
  </div>
  <div class="abs hours-card" style="left:722px">
    <div class="hours-title"><svg width="24" height="22" viewBox="0 0 24 22"><path d="M1 3L8 0L16 3L23 0V19L16 22L8 19L1 22Z" fill="#4a1505"/><path d="M8 0V19M16 3V22" stroke="#fff" stroke-width="1.5"/></svg>Location</div>
    <div class="hours-line" style="top:68px"><svg width="9" height="11" viewBox="0 0 9 11"><path d="M4.5 0A4.5 4.5 0 0 1 9 4.5C9 7 4.5 11 4.5 11S0 7 0 4.5A4.5 4.5 0 0 1 4.5 0Z" fill="#3b2a20"/><circle cx="4.5" cy="4.5" r="1.6" fill="#fff"/></svg> 2140 Pinecrest Road<br>&nbsp;&nbsp;&nbsp;Ridgeway AL 35990</div>
    <div class="hours-line" style="top:108px"><svg width="10" height="10" viewBox="0 0 10 10"><path d="M2 0L4 2.5L3 4Q4.5 6.5 6 7L7.5 6L10 8L8.5 10Q3 9 0 1.5Z" fill="#3b2a20"/></svg> (205) 555-0143</div>
    <div class="hours-band"><svg width="11" height="11" viewBox="0 0 11 11"><circle cx="5.5" cy="5.5" r="4.6" fill="none" stroke="#fff" stroke-width="1.4"/><path d="M5.5 2.5V5.5H8" stroke="#fff" stroke-width="1.4" fill="none"/></svg> <span>Mon - Sat: 11:00 am<br>- 12:00 am/midnight</span></div>
  </div>
</section>

<section>
  <div class="abs news-bg"></div>
  <svg class="abs news-edge" width="1200" height="16" aria-hidden="true">
    <defs><pattern id="scallop" width="16" height="16" patternUnits="userSpaceOnUse"><circle cx="8" cy="16" r="8" fill="#fbeed8"/></pattern></defs>
    <rect width="1200" height="16" fill="url(#scallop)"/>
  </svg>
  <h2 class="abs heading news-title">News &amp; Event</h2>

  <article class="abs news-item" style="left:149px">
    <div class="news-photo" style="background:linear-gradient(160deg,#c9c6c0,#7a6e64 55%,#2e2822)" role="img" aria-label="Tongs turning brisket over a smoking grill"></div>
    <h3>Best BB Qs</h3>
    <p>Lorem Ipsum is simply dummy text of the printing and typesetting industry. Lorem Ipsum has been the</p>
  </article>
  <article class="abs news-item" style="left:453px">
    <div class="news-photo" style="background:linear-gradient(180deg,#132536,#2a3f52 45%,#8a4a2e 75%,#2a201c)" role="img" aria-label="Meat on a smoker grate under blue smoke"></div>
    <h3>Best BB Qs</h3>
    <p>Lorem Ipsum is simply dummy text of the printing and typesetting industry. Lorem Ipsum has been the</p>
  </article>
  <article class="abs news-item" style="left:757px">
    <div class="news-photo" style="background:linear-gradient(180deg,#2a1c16,#8a3a24 40%,#a4563a 65%,#3a2a24)" role="img" aria-label="Racks of smoked pork shoulders inside a pit"></div>
    <h3>Best BB Qs</h3>
    <p>Lorem Ipsum is simply dummy text of the printing and typesetting industry. Lorem Ipsum has been the</p>
  </article>
</section>

<footer>
  <div class="abs site-footer"></div>
  <div class="abs copyright">Copyright 2017 Dunmore Smokehouse, LLC</div>
  <nav class="abs footer-nav"><span>Home</span><span>About</span><span>Locations</span><span>Restaurant Menus</span><span>Catering</span><span>News</span><span>Store</span><span>Contact Us</span></nav>
</footer>

</body>
</html>
```